New web design for a service provider in the medical field

We are looking for a new design for our website. We are a company that repairs and sells medical endoscopes. Our customers include doctors and hospitals. Our current website can be found at https://lumenfix.example/en/lumenfix-english.
We need a new web design (without programming) for the following 3 pages:
-Startpage https://lumenfix.example/en/lumenfix-english/
-Used endoscopes https://lumenfix.example/en/used-endoscopes/
-Purchase https://lumenfix.example/en/purchase/
The design should be modern and stylish.
The blue color of the logo should be reflected on the page, but not too intrusive.
I have uploaded the images from the header. If more images are needed, let me know and I will upload them.

Target Market(s)
Doctors and hospitals

```html
<!DOCTYPE html>
<html lang="en">
<head>
<meta charset="utf-8">
<title>About lumenFIX</title>
<link rel="stylesheet" href="https://fonts.googleapis.com/css2?family=Outfit:wght@300;400;500;600;700&display=swap">
<style>
:root{
  --brand:#29a8e0;
  --brand-deep:#0857ad;
  --brand-mid:#0b78c8;
  --ink:#1c3344;
  --text:#3d4650;
  --line:#e3e8ec;
  --white:#ffffff;
}
*{box-sizing:border-box;margin:0;padding:0}
html,body{width:1200px;height:2434px;overflow:hidden;background:var(--white)}
body{font-family:"Outfit",sans-serif;color:var(--text);position:relative}
.abs{position:absolute}
a{color:inherit;text-decoration:none}

/* top bar */
.topbar{left:0;top:0;width:1200px;height:33px;background:var(--brand);color:var(--white);font-size:12.5px;font-weight:600}
.topbar .follow{left:101px;top:0;height:33px;display:flex;align-items:center;gap:10px}
.dot{width:24px;height:24px;border-radius:50%;background:var(--white);display:inline-block}
.dot.dark{background:var(--ink)}
.dot.outline{background:transparent;border:2px solid var(--white)}
.topbar .links{right:68px;top:0;height:33px;display:flex}
.topbar .links a{padding:0 16px;line-height:33px;border-left:1px solid rgba(255,255,255,.5)}
.topbar .links a:first-child{border-left:none}

/* header */
.logo{font-weight:600;color:var(--ink);display:flex;align-items:center;gap:8px;letter-spacing:.3px}
.logo .mark{width:14px;height:14px;border-radius:50%;background:var(--brand)}
.header-logo{left:102px;top:80px;font-size:23px}
.contact{top:57px;display:flex;align-items:center;gap:8px}
.contact .ic{width:23px;height:23px;border-radius:50%;background:var(--brand);display:flex;align-items:center;justify-content:center}
.contact small{display:block;font-size:11px;color:var(--brand);font-weight:500;line-height:1.1}
.contact span{font-size:13.5px;color:var(--ink);font-weight:500}
.lang{left:997px;top:60px;font-size:13px;font-weight:600;color:var(--ink);display:flex;align-items:center;gap:6px}
.lang i{width:15px;height:11px;background:#c8102e;display:inline-block;border-radius:1px}
.nav{left:285px;top:110px;display:flex;gap:30px;font-size:13px;font-weight:500;color:var(--ink)}
.nav .active{border-bottom:2px solid var(--brand);padding-bottom:3px}

/* hero */
.hero{left:0;top:158px;width:1200px;height:520px}
.hero-kicker{left:109px;top:338px;font-size:28px;font-weight:400;color:var(--brand)}
.hero-title{left:109px;top:368px;font-size:41px;font-weight:700;color:var(--ink)}

/* intro */
.intro-head{left:0;top:748px;width:1200px;text-align:center;font-size:37px;font-weight:700;line-height:45px;color:var(--ink)}
.intro-head em{font-style:normal;color:var(--brand)}
.rule{height:3px;width:71px;background:var(--brand)}
.intro-text{left:608px;top:918px;width:500px;font-size:17.5px;line-height:27px;font-weight:300;color:var(--text)}
.intro-text p+p{margin-top:11px}

/* why section */
.why-title{left:0;top:1487px;width:1200px;text-align:center;font-size:34px;font-weight:300;color:var(--white)}
.why-title b{font-weight:700}
.feat{color:var(--white);font-size:13px;line-height:18px;font-weight:300}
.feat h3{font-size:19px;font-weight:600;margin-bottom:4px;line-height:24px}
.feat.left{text-align:right}
.hex-logo{left:502px;top:1715px;width:200px;text-align:center;font-size:23px;justify-content:center}

/* footer */
.foot-logo{left:138px;top:2174px;font-size:23px}
.divider{width:1px;height:210px;background:var(--line)}
.col h4{font-size:15px;font-weight:600;color:var(--ink);border-left:3px solid var(--brand);padding-left:16px;height:22px;line-height:22px;margin-bottom:12px}
.col a{display:block;font-size:14.5px;color:var(--ink);font-weight:300;padding-left:19px;line-height:29px}
.badge{left:898px;top:2234px;width:120px;height:80px;background:linear-gradient(#1d3f8f 0 68%,#f07c1a 68%)}
.bottom-line{left:0;top:2365px;width:1200px;height:1px;background:var(--line)}
.copy{left:0;top:2386px;width:1200px;text-align:center;font-size:13px;color:#5b6670;font-weight:300}
</style>
</head>
<body>

<div class="abs topbar">
  <div class="abs follow">FOLLOW US <i class="dot"></i><i class="dot outline"></i></div>
  <nav class="abs links"><a href="#">PICK-UP ORDER</a><a href="#">ABOUT US</a><a href="#">CONTACT US</a></nav>
</div>

<div class="abs logo header-logo"><i class="mark"></i>lumenFIX</div>

<div class="abs contact" style="left:622px">
  <div class="ic"><svg width="12" height="9" viewBox="0 0 12 9"><rect x=".5" y=".5" width="11" height="8" fill="none" stroke="#fff"/><path d="M.5 .5 6 5 11.5 .5" fill="none" stroke="#fff"/></svg></div>
  <div><small>EMAIL US</small><span>info@lumenfix.example</span></div>
</div>
<div class="abs contact" style="left:806px">
  <div class="ic"><svg width="12" height="12" viewBox="0 0 12 12"><path d="M2 1 4 1 5 4 3.5 5A7 7 0 0 0 7 8.5L8 7l3 1v2c0 .6-.4 1-1 1A9 9 0 0 1 1 2c0-.6.4-1 1-1z" fill="#fff"/></svg></div>
  <div><small>CALL US NOW</small><span>+49 4100 555 010-0</span></div>
</div>
<div class="abs lang"><i></i>ENG <svg width="10" height="7" viewBox="0 0 10 7"><path d="M1 1l4 4 4-4" fill="none" stroke="#1c3344" stroke-width="1.6"/></svg></div>

<nav class="abs nav">
  <a href="#">HOME</a><a href="#">ENDOSOPE REPAIR</a><a href="#">USED ENDOSCOPES</a><a href="#">ENDOSCOPY SYSTEMS</a><a href="#">ENDOSCOPY ACCESSORIES</a><a href="#" class="active">PURCHASE</a>
</nav>

<svg class="abs hero" viewBox="0 0 1200 520" role="img" aria-label="Flexible endoscope and processor unit on a white workbench">
  <defs>
    <linearGradient id="heroFill" x1="0" x2="1" y1="0" y2="0">
      <stop offset="0" stop-color="#f1f1f3"/><stop offset=".4" stop-color="#ececee"/><stop offset=".7" stop-color="#cfd3d8"/><stop offset="1" stop-color="#b9bec5"/>
    </linearGradient>
  </defs>
  <polygon points="0,0 1200,0 1200,416 600,516 0,416" fill="url(#heroFill)"/>
  <polygon points="0,418 600,512 1200,418 1200,432 600,518 0,436" fill="var(--brand)"/>
</svg>
<div class="abs hero-kicker">WHO WE ARE</div>
<div class="abs hero-title">ABOUT LUMEN FIX</div>

<h1 class="abs intro-head">WE ARE YOUR EXPERTS FOR REPAIRING<br><em>FLEXIBLE ENDOSCOPES!</em></h1>
<div class="abs rule" style="left:565px;top:849px"></div>

<svg class="abs" style="left:121px;top:867px" width="444" height="444" viewBox="0 0 444 444">
  <circle cx="222" cy="222" r="220" fill="none" stroke="#9fd6ef" stroke-width="2"/>
  <circle cx="222" cy="222" r="208" fill="none" stroke="var(--brand)" stroke-width="2"/>
  <circle cx="222" cy="222" r="201" fill="#e4e5e7" role="img" aria-label="Close-up of an endoscope control handle"/>
</svg>

<div class="abs intro-text">
  <p>lumenFIX GmbH is specialized in repairing and saling flexible endoscopes along with accessories and consumables. We offer endoscopes, processors, light sources, accessories and much more – with a focus on the manufacturers Orvane, Pentora and Fujara. For sale on our part only refurbished equipment is offered, because quality is our highest claim!</p>
  <p>We applied for foundation in 2020, whereby lumenFIX emerged from another company in the same business field. For this reason, all employees have many years of specific experience in the business field. As a service-oriented company, lumenFIX is certified (DIN ISO 9001:2015) and is at your disposal with all its capabilities. Customers in Germany can make use of our loaner equipment service.</p>
</div>

<svg class="abs" style="left:0;top:1360px" width="1200" height="720" viewBox="0 0 1200 720">
  <defs>
    <linearGradient id="whyFill" x1="0" y1="0" x2="1" y2="1">
      <stop offset="0" stop-color="var(--brand-deep)"/><stop offset=".55" stop-color="var(--brand-mid)"/><stop offset="1" stop-color="#16aee6"/>
    </linearGradient>
  </defs>
  <polygon points="0,97 600,10 1200,97 1200,140 0,140" fill="var(--brand)"/>
  <polygon points="0,104 600,24 1200,104 1200,629 612,712 0,629" fill="url(#whyFill)"/>
  <polygon points="0,629 612,712 1200,629 1200,634 612,722 0,636" fill="#dff1fa"/>
  <!-- hexagon -->
  <polygon points="602,237 725,308 725,450 602,521 479,450 479,308" fill="none" stroke="#5fb4e6" stroke-width="2"/>
  <polygon points="602,250 714,315 714,443 602,508 490,443 490,315" fill="var(--white)"/>
  <polygon points="602,259 706,320 706,438 602,499 498,438 498,320" fill="none" stroke="var(--brand)" stroke-width="2"/>
  <!-- connectors -->
  <g fill="none" stroke="#ffffff" stroke-width="1.4">
    <path d="M448 262H478L512 298"/>
    <path d="M756 272H726L692 306"/>
    <path d="M446 490H478L512 454"/>
    <path d="M758 487H726L692 452"/>
    <circle cx="412" cy="262" r="33"/><circle cx="795" cy="272" r="33"/>
    <circle cx="410" cy="490" r="33"/><circle cx="798" cy="487" r="33"/>
    <!-- calendar -->
    <rect x="398" y="248" width="24" height="24" rx="2"/><path d="M398 255H422M404 244V251M416 244V251"/><circle cx="424" cy="274" r="6"/><path d="M424 271v3h2"/>
    <!-- shield -->
    <path d="M795 255l14 5v10c0 9-6 15-14 18-8-3-14-9-14-18v-10z"/><path d="M788 271l5 5 9-9"/>
    <!-- clock -->
    <circle cx="410" cy="490" r="15"/><circle cx="410" cy="490" r="11"/><path d="M410 482v8l5 4"/>
    <!-- hand with card -->
    <rect x="790" y="470" width="16" height="12" rx="1"/><path d="M794 475h8M794 479h5M782 500l6-6h8l4 3h8"/>
  </g>
</svg>

<h2 class="abs why-title">WHY <b>CHOOSE US</b></h2>
<div class="abs rule" style="left:558px;top:1537px;width:88px"></div>

<div class="abs logo hex-logo"><i class="mark"></i>lumenFIX</div>

<div class="abs feat left" style="left:110px;top:1588px;width:243px">
  <h3>Years of experience</h3>
  The company may just have been founded, but the whole team has tons of experience in the business field. – We are very familiar with endoscopes!
</div>
<div class="abs feat left" style="left:105px;top:1800px;width:250px">
  <h3>Fast repair service</h3>
  We work quickly and thoroughly, pursuing the goal of keeping the restrictions in your doctor's office or hospital as low as possible in the case of any defect in your endoscope technology.
</div>
<div class="abs feat" style="left:849px;top:1600px;width:250px">
  <h3>Competent specialists</h3>
  The quality of our work and our confidence in our work results are shown by the extensive warrenties that we give on used and refurbished devices.
</div>
<div class="abs feat" style="left:849px;top:1807px;width:250px">
  <h3>Brand-independent advices</h3>
  Your customer satisfaction is our focus and not the sales numbers for a specific product or the products of a specific manufacturer!
</div>

<div class="abs logo foot-logo"><i class="mark"></i>lumenFIX</div>
<div class="abs divider" style="left:425px;top:2100px"></div>
<div class="abs divider" style="left:666px;top:2100px"></div>
<div class="abs divider" style="left:872px;top:2100px"></div>

<div class="abs col" style="left:425px;top:2152px">
  <h4>NAVIGATION</h4>
  <a href="#">Home</a><a href="#">Endoscope Repair</a><a href="#">Used Endoscope</a><a href="#">Endoscopy Systems</a>
</div>
<div class="abs col" style="left:665px;top:2152px">
  <h4>RESOURCES</h4>
  <a href="#">Endoscopy Accesories</a><a href="#">Purchase</a><a href="#">Contact Us</a>
</div>
<div class="abs col" style="left:872px;top:2152px">
  <h4>FOLLOW US</h4>
  <div style="padding-left:26px;display:flex;gap:10px"><i class="dot dark" style="width:31px;height:31px"></i><i class="dot dark" style="width:31px;height:31px"></i></div>
</div>
<div class="abs badge" role="img" aria-label="Quality management certificate"></div>

<div class="abs bottom-line"></div>
<div class="abs copy">© 2022 lumenFIX GmbH All Right Reserved</div>

</body>
</html>
```